Orvane KT Migration

We are currently creating a campaign to raise the awareness of the public of the end of support for Orvane KT.

We will provide the end-end migration from Orvan KT - Orvane 6.2.

It wll include
1) Analysing requirement (Non-supported software/ hardware / purchasing of hardware)
2) Backup of Data
3) Installing of new Operating system
4) Installing of new apps, restore of Data & configuration
5) Testing & validation after migration

Please feel free to explore your creativity

Hi All,

Some additional info of the project is provided below:
https://cdn.filqora.net/u/83726150/flyer.zip

```html
<!DOCTYPE html>
<html lang="en">
<head>
<meta charset="utf-8">
<title>Transition to Orvane 6 – Velmora Consulting</title>
<link rel="stylesheet" href="https://fonts.googleapis.com/css2?family=Arimo:wght@700&family=Tinos:wght@400;700&display=swap">
<style>
  :root {
    --cream: #f8f6e9;
    --band-green: #8fb043;
    --band-green-dark: #7fa036;
    --white: #ffffff;
    --ink: #111111;
    --act-green: #7a9c2e;
    --teal-deep: #3a8a8c;
    --teal-bright: #3cb3bd;
    --teal-light: #45bcc8;
    --green-dark: #4b6a2f;
    --green-mid: #8aa83a;
    --green-soft: #a0b442;
    --logo-grey: #3a3a3a;
  }
  * { margin: 0; padding: 0; box-sizing: border-box; }
  html, body { width: 932px; height: 1200px; overflow: hidden; background: var(--cream); }
  .flyer { position: relative; width: 932px; height: 1200px; background: var(--cream); overflow: hidden; }

  .header-band {
    position: absolute; left: 0; top: 0; width: 932px; height: 241px;
    background: linear-gradient(180deg, var(--band-green) 0%, var(--band-green-dark) 100%);
  }
  .header-kicker {
    position: absolute; left: 65px; top: 44px;
    font: 700 25px "Arimo", Arial, sans-serif; color: var(--white); letter-spacing: 0.5px;
  }
  .header-title { position: absolute; left: 0; top: 0; width: 932px; height: 241px; }
  .header-title text { font-family: "Arimo", Arial, sans-serif; font-weight: 700; fill: var(--white); }

  .company-name {
    position: absolute; left: 0; top: 286px; width: 932px; text-align: center;
    font: 400 64px "Tinos", "Times New Roman", serif; color: var(--ink); letter-spacing: 1px;
  }
  .company-strap {
    position: absolute; left: 0; top: 346px; width: 932px; text-align: center;
    font: 700 25px "Tinos", "Times New Roman", serif; color: var(--ink);
  }

  .process-art {
    position: absolute; left: 133px; top: 414px; width: 696px; height: 756px;
    background:
      radial-gradient(ellipse 48% 40% at 50% 40%, rgba(150,190,80,0.35), rgba(150,190,80,0) 100%),
      radial-gradient(ellipse 30% 50% at 50% 95%, rgba(60,170,185,0.25), rgba(60,170,185,0) 100%);
  }

  .step {
    position: absolute; border-radius: 50%; display: flex; align-items: center; justify-content: center;
    text-align: center; color: var(--white); font-family: "Tinos", "Times New Roman", serif; font-weight: 700;
    line-height: 1.15;
  }
  .step-analyse  { left: 341px; top: 429px; width: 186px; height: 186px; background: var(--teal-deep); font-size: 30px; }
  .step-backup   { left: 199px; top: 540px; width: 134px; height: 134px; background: var(--teal-bright); font-size: 24px; }
  .step-install-os { left: 540px; top: 551px; width: 142px; height: 142px; background: var(--teal-light); font-size: 23px; }
  .step-apps     { left: 338px; top: 652px; width: 162px; height: 162px; background: var(--green-dark); font-size: 26px; }
  .step-restore  { left: 533px; top: 730px; width: 148px; height: 148px; background: var(--green-mid); font-size: 22px; }
  .step-testing  { left: 387px; top: 846px; width: 134px; height: 134px; background: var(--green-soft); font-size: 20px; }

  .call-to-action {
    position: absolute; left: 59px; top: 1050px;
    font: 700 30px "Tinos", "Times New Roman", serif; color: var(--act-green); text-decoration: underline;
  }
  .contact-list {
    position: absolute; left: 59px; top: 1092px; list-style: none;
    font: 700 19px "Tinos", "Times New Roman", serif; color: var(--ink); line-height: 28px;
  }

  .brand-name {
    position: absolute; left: 655px; top: 1088px; width: 220px; text-align: center;
    font: 400 52px "Tinos", "Times New Roman", serif; color: var(--logo-grey); letter-spacing: 1px;
  }
</style>
</head>
<body>
<main class="flyer">
  <header class="header-band">
    <p class="header-kicker">ORVANE KT IS UNSECURE!!</p>
    <svg class="header-title" viewBox="0 0 932 241" aria-label="Transition to Orvane 6">
      <text x="59" y="197" font-size="150" textLength="814" lengthAdjust="spacingAndGlyphs">TRANSITION</text>
      <text x="814" y="224" font-size="37" text-anchor="end">TO ORVANE 6</text>
    </svg>
  </header>

  <h1 class="company-name">VELMORA CONSULTING</h1>
  <p class="company-strap">MAKES IT EASY:</p>

  <div class="process-art" role="img" aria-label="Illustration of a tree made of green and teal circuit lines and small icons, growing from a laptop"></div>

  <div class="step step-analyse">Analysing<br>Requirement</div>
  <div class="step step-backup">Backing<br>Up Data</div>
  <div class="step step-install-os">Installing<br>Operating<br>System</div>
  <div class="step step-apps">Installing<br>New Apps</div>
  <div class="step step-restore">Restoring<br>Data &amp;<br>Configuration</div>
  <div class="step step-testing">Testing<br>&amp;<br>Validating</div>

  <p class="call-to-action">ACT NOW!</p>
  <ul class="contact-list">
    <li>P: (555) 201-4400</li>
    <li>F: (555) 201-4401</li>
    <li>E: VelmoraConsult@velmora.net</li>
  </ul>

  <p class="brand-name">VELMORA</p>
</main>
</body>
</html>
```